I need a wordpress website for myconsulting company specialized in data privacy

I'm looking for a wordpress website for my consulting company specialized in data privacy (GDPR) and computer science.
The website will serve as entry point to for potential clients.
The website should have the following sections (I'm opened to new ideas):
- Presentation of the company
- General presentation
- Services provided with some details
- Blog/articles with tags (if possible)
- Contact
On every page of the website there should be some references to pages (such as privacy policy, legal information...)
If possible he website should be multinlingual (english and french). I'll personnally take care of the translation in french.
Regarding branding;
- Name of the company: Étienne Roubaud Conseil
- Logo is attached
- For colors to be used see attached PDF for exemple

```html
<!DOCTYPE html>
<html lang="en">
<head>
<meta charset="utf-8">
<title>Étienne Roubaud Conseil — Data Privacy &amp; Computer Science</title>
<link rel="stylesheet" href="https://fonts.googleapis.com/css2?family=Lexend+Exa:wght@300;400&family=Montserrat:wght@400;500;600&display=swap">
<style>
:root{
  --teal:#138c9a;
  --teal-soft:#3aa9b5;
  --navy:#0d2536;
  --ink:#2a2a2a;
  --muted:#6d6d6d;
  --paper:#ffffff;
  --mist:#f4f4f4;
  --mist-strip:#ebebeb;
  --footer:#252525;
  --line:#3f3f3f;
}
*{box-sizing:border-box;margin:0;padding:0}
html,body{width:1200px;height:3951px;overflow:hidden}
body{position:relative;background:var(--paper);font-family:"Montserrat",sans-serif;color:var(--ink)}
.abs{position:absolute}
.display{font-family:"Lexend Exa",sans-serif;font-weight:300;letter-spacing:-1px}
.btn{position:absolute;display:flex;align-items:center;justify-content:center;border:1.5px solid #555;border-radius:30px;font-size:17px;font-weight:500;color:var(--ink);text-transform:uppercase;letter-spacing:.2px;background:transparent}
.copy{font-size:16.5px;line-height:26px;color:var(--muted)}

/* hero */
.hero{position:absolute;left:0;top:0;width:1200px;height:730px}
.hero-photo{position:absolute;inset:0;clip-path:polygon(0 0,100% 0,100% 628px,0 725px);
  background:radial-gradient(ellipse at 78% 45%,#3a5563 0%,#1a2c38 35%,transparent 70%),linear-gradient(100deg,#0d3a55 0%,#0f2739 40%,#151a20 100%)}
.hero-band{position:absolute;left:0;top:0}
.topbar{position:absolute;top:24px;left:513px;display:flex;gap:14px;align-items:center;color:#fff;font-size:17px;font-weight:600}
.topbar svg{vertical-align:-2px;margin-right:4px}
.nav{position:absolute;top:76px;left:0;width:1200px;height:24px}
.nav a{position:absolute;color:#fff;font-size:16px;font-weight:600;text-decoration:none}
.nav a.is-active{color:var(--teal-soft)}
.brand{position:absolute;display:flex;align-items:center;gap:10px;color:#fff;font-family:"Lexend Exa",sans-serif;font-weight:300}
.brand-mark{border:2px solid #fff}
.hero-kicker{position:absolute;left:112px;top:252px;color:#fff;font-size:24px;font-weight:500}
.hero-title{position:absolute;left:110px;top:306px;color:#fff;font-size:50px;line-height:59px}
.hero .btn{border-color:#fff;color:#fff;left:112px;top:526px;width:376px;height:63px;font-size:18px;font-weight:600}

/* welcome */
.welcome-frame{position:absolute;left:86px;top:795px;width:494px;height:466px;border-radius:24px;background:var(--teal-soft)}
.welcome-inner{position:absolute;left:56px;top:54px;width:380px;height:372px;background:#fff;border-radius:10px}
.welcome-photo{position:absolute;left:24px;top:0;width:356px;height:342px;background:linear-gradient(135deg,#d9d2cb,#8e8c8d 55%,#4b4b55)}
.welcome-title{position:absolute;left:656px;top:796px;font-size:42px;line-height:50px;color:var(--ink)}

/* services */
.services-bg{position:absolute;left:0;top:1300px}
.section-title{position:absolute;left:0;width:1200px;text-align:center;font-size:41px;color:var(--ink)}
.service-photo{position:absolute;width:300px;height:300px;border-radius:50%;box-shadow:0 6px 10px rgba(0,0,0,.25)}
.service-name{position:absolute;font-size:26px;font-weight:500;color:var(--ink)}

/* blog */
.card{position:absolute;top:2383px;width:311px}
.card-photo{height:226px;border-radius:8px;position:relative}
.card-tag{position:absolute;left:0;top:0;background:var(--teal);color:#fff;font-size:15px;font-weight:600;padding:4px 6px;border-top-left-radius:8px}
.card h3{font-size:21px;font-weight:500;margin:24px 0 0 3px}
.card .meta{font-size:16px;color:var(--muted);margin:13px 0 0 3px;display:flex;gap:7px;align-items:center}
.card .copy{margin:20px 0 0 0}
.card .btn{position:relative;width:157px;height:51px;margin-top:26px}

/* contact */
.contact-photo{position:absolute;left:0;top:2943px;width:436px;height:632px;background:linear-gradient(140deg,#e9eef2,#b8c4cc 55%,#7d8790)}
.contact-panel{position:absolute;left:436px;top:2943px;width:764px;height:632px;background:var(--teal)}
.contact-title{position:absolute;left:494px;top:3000px;color:#fff;font-size:43px}
.field{position:absolute;background:#fff;color:#666;font-size:16px;padding:14px 16px}
.send{position:absolute;left:496px;top:3425px;width:121px;height:55px;border:1.5px solid #fff;border-radius:30px;color:#fff;font-weight:600;font-size:18px;display:flex;align-items:center;justify-content:center}

/* footer */
.footer-bg{position:absolute;left:0;top:3560px}
.foot-head{position:absolute;color:#fff;font-size:18px;font-weight:600}
.foot-links{position:absolute;left:598px;top:3680px;list-style:none;color:#fff;font-size:16px;line-height:28px}
.foot-info{position:absolute;color:#fff;font-size:16px;line-height:25px}
.foot-rule{position:absolute;left:110px;top:3866px;width:978px;height:1px;background:var(--line)}
.legal{position:absolute;left:110px;top:3897px;color:#fff;font-size:16px}
.legal strong{font-weight:600}
.social{position:absolute;top:3886px;width:42px;height:42px;border:1.5px solid #fff;border-radius:50%}
</style>
</head>
<body>

<!-- Hero -->
<header class="hero">
  <div class="hero-photo" role="img" aria-label="Photo of hands typing on a laptop with a glowing padlock and login interface overlay"></div>
  <svg class="hero-band" width="1200" height="730" viewBox="0 0 1200 730" aria-hidden="true">
    <polygon points="0,722 1200,626 1200,664 0,727" fill="var(--teal)"/>
  </svg>

  <div class="brand" style="left:110px;top:40px;font-size:22px">
    <span class="brand-mark" style="width:22px;height:22px"></span>Étienne Roubaud Conseil
  </div>

  <div class="topbar">
    <span><svg width="14" height="14" viewBox="0 0 24 24"><path fill="#fff" d="M6.6 10.8a15 15 0 006.6 6.6l2.2-2.2c.3-.3.7-.4 1-.2 1.1.4 2.3.6 3.6.6.6 0 1 .4 1 1V20c0 .6-.4 1-1 1A17 17 0 013 4c0-.6.4-1 1-1h3.5c.6 0 1 .4 1 1 0 1.3.2 2.5.6 3.6.1.3 0 .7-.2 1z"/></svg>1 555 014 2090</span>
    <span>|</span>
    <span><svg width="16" height="13" viewBox="0 0 24 18"><rect x="1" y="1" width="22" height="16" rx="2" fill="#fff"/><path d="M2 3l10 7 10-7" stroke="#13232e" stroke-width="2" fill="none"/></svg>info@etienneroubaud-conseil.com</span>
    <span style="margin-left:4px">Eng <svg width="9" height="6" viewBox="0 0 10 6"><path d="M1 1l4 4 4-4" stroke="#fff" stroke-width="1.5" fill="none"/></svg></span>
  </div>

  <nav class="nav">
    <a class="is-active" style="left:563px">HOME</a>
    <a style="left:657px">ABOUT US</a>
    <a style="left:787px">SERVICES</a>
    <a style="left:913px">BLOG</a>
    <a style="left:1002px">CONTACT</a>
  </nav>

  <p class="hero-kicker">We Specialized in</p>
  <h1 class="hero-title display">Data privacy<br>(GDPR) and<br>Computer Science.</h1>
  <a class="btn">Request a free consultation</a>
</header>

<!-- Welcome -->
<section>
  <div class="welcome-frame">
    <div class="welcome-inner">
      <div class="welcome-photo" role="img" aria-label="Photo of a business team meeting around a laptop in an office"></div>
    </div>
  </div>
  <h2 class="welcome-title display">Welcome to<br>Étienne Roubaud<br>Conseil</h2>
  <p class="copy abs" style="left:658px;top:970px;width:440px">Lorem ipsum dolor sit amet, consectetur adipiscing elit, sed do eiusmod tempor incididunt ut labore et dolore magna aliqua. Ut enim ad minim veniam, quis nostrud exercitation ullamco laboris nisi ut aliquip ex ea commodo consequat. Duis aute irure dolor in rpre henderit in voluptate velit esse cillum dolore eu fugat nulla pariat cepteur sint occaecat.</p>
  <a class="btn" style="left:658px;top:1195px;width:157px;height:51px">Read more</a>
</section>

<!-- Services -->
<section>
  <svg class="services-bg" width="1200" height="932" viewBox="0 0 1200 932" aria-hidden="true">
    <polygon points="0,72 1200,12 1200,40 0,109" fill="var(--mist-strip)"/>
    <polygon points="0,109 1200,40 1200,932 0,932" fill="var(--mist)"/>
  </svg>
  <h2 class="section-title display" style="top:1426px">Our Services</h2>

  <svg class="abs" style="left:110px;top:1545px" width="124" height="124" viewBox="0 0 124 124" fill="none" stroke="#1c2a4a" stroke-width="3" aria-hidden="true">
    <path d="M24 58C8 58 4 38 18 32 18 12 44 6 54 20 66 4 94 10 94 32 112 32 118 56 100 60"/>
    <path d="M26 44h46l14 14v60H26z"/><path d="M72 44v14h14"/>
    <path d="M36 70h36M36 82h30M36 94h26M36 106h24"/>
    <rect x="78" y="86" width="30" height="28" rx="3" stroke="var(--teal)"/>
    <path d="M84 86v-8a9 9 0 0118 0v8" stroke="var(--teal)"/>
  </svg>
  <p class="service-name" style="left:113px;top:1690px">Data Privacy (GDPR)</p>
  <div class="service-photo" style="left:445px;top:1519px;background:linear-gradient(135deg,#2aa5b8,#13506b 50%,#7b6a5c)" role="img" aria-label="Photo of hands at a laptop with a glowing security shield"></div>
  <p class="copy abs" style="left:778px;top:1542px;width:320px;font-size:16px;line-height:25.7px">Nemo enim ipsam voluptatem quia vo luptas sit aspernatur aut odit aut fugit, sed quia consequuntur magni dolores eos qui ratione voluptatem sequi nesc iunt. Neque porro quisquam est, quido lorem ipsum quia dolor sit amet, cons ectetur, adipisci velit,..</p>
  <a class="btn" style="left:778px;top:1745px;width:157px;height:51px">Read more</a>

  <p class="copy abs" style="left:115px;top:1875px;width:320px;font-size:16px;line-height:25.7px">Nemo enim ipsam voluptatem quia vo luptas sit aspernatur aut odit aut fugit, sed quia consequuntur magni dolores eos qui ratione voluptatem sequi nesc iunt. Neque porro quisquam est, quido lorem ipsum quia dolor sit amet, cons ectetur, adipisci velit,..</p>
  <a class="btn" style="left:115px;top:2078px;width:157px;height:51px">Read more</a>
  <div class="service-photo" style="left:445px;top:1852px;background:radial-gradient(circle at 50% 45%,#e8f2ff,#5c7fa6 40%,#1c2e4a 80%)" role="img" aria-label="Photo of a hand holding a phone surrounded by network icons"></div>
  <svg class="abs" style="left:786px;top:1887px" width="112" height="112" viewBox="0 0 112 112" fill="none" stroke="#1c2a4a" stroke-width="3" aria-hidden="true">
    <path d="M28 6h38l14 14v56H28z"/><path d="M66 6v14h14"/>
    <path d="M38 22h22M38 32h30M50 44h22"/>
    <rect x="58" y="50" width="14" height="14" stroke="var(--teal)"/>
    <circle cx="40" cy="62" r="9" stroke="var(--teal)"/><circle cx="40" cy="62" r="3" stroke="var(--teal)"/>
    <rect x="10" y="20" width="92" height="70" rx="3"/><path d="M2 96h108v6H2z"/>
  </svg>
  <p class="service-name" style="left:786px;top:2024px">Computer Science</p>
</section>

<!-- Blog -->
<section>
  <h2 class="section-title display" style="top:2294px">Our Blog</h2>

  <article class="card" style="left:110px">
    <div class="card-photo" style="background:linear-gradient(135deg,#cdd1d0,#8a8076 55%,#4a4440)" role="img" aria-label="Photo of colleagues reviewing documents on a table"><span class="card-tag">DATA PRIVACY</span></div>
    <h3>Finibus Bonoruet Maldror</h3>
    <p class="meta"><span>▦ 22/02/2022</span><span>|</span><span>● Admin</span></p>
    <p class="copy">Nam libero tempore, cum soluta nbis est eligendi optio cumque nihil impe dit quo minus id quo.</p>
    <a class="btn">Read more</a>
  </article>

  <article class="card" style="left:445px">
    <div class="card-photo" style="background:linear-gradient(135deg,#d8b89a,#a97a58 50%,#6c4a35)" role="img" aria-label="Photo of a person using a smartphone with app icons"><span class="card-tag">COMPUTER SCIENCE</span></div>
    <h3>Finibus Bonoruet Maldror</h3>
    <p class="meta"><span>▦ 22/02/2022</span><span>|</span><span>● Admin</span></p>
    <p class="copy">Nam libero tempore, cum soluta nbis est eligendi optio cumque nihil impe dit quo minus id quo.</p>
    <a class="btn">Read more</a>
  </article>

  <article class="card" style="left:778px">
    <div class="card-photo" style="background:linear-gradient(135deg,#5b6a86,#9aa3b8 50%,#dfe1e8)" role="img" aria-label="Photo of two coworkers looking at a computer screen"><span class="card-tag">DATA PRIVACY</span></div>
    <h3>Finibus Bonoruet Maldror</h3>
    <p class="meta"><span>▦ 22/02/2022</span><span>|</span><span>● Admin</span></p>
    <p class="copy">Nam libero tempore, cum soluta nbis est eligendi optio cumque nihil impe dit quo minus id quo.</p>
    <a class="btn">Read more</a>
  </article>
</section>

<!-- Contact -->
<section>
  <div class="contact-photo" role="img" aria-label="Photo of hands typing on a laptop keyboard"></div>
  <div class="contact-panel"></div>
  <h2 class="contact-title display">Contact Us</h2>
  <div class="field" style="left:497px;top:3086px;width:292px;height:49px">First Name</div>
  <div class="field" style="left:804px;top:3086px;width:292px;height:49px">Last Name</div>
  <div class="field" style="left:497px;top:3147px;width:292px;height:49px">Email</div>
  <div class="field" style="left:804px;top:3147px;width:292px;height:49px">Address</div>
  <div class="field" style="left:497px;top:3210px;width:601px;height:49px">Company Name</div>
  <div class="field" style="left:497px;top:3272px;width:601px;height:125px">Message</div>
  <div class="send">SEND</div>
</section>

<!-- Footer -->
<footer>
  <svg class="footer-bg" width="1200" height="391" viewBox="0 0 1200 391" aria-hidden="true">
    <polygon points="0,27 1200,0 1200,391 0,391" fill="var(--paper)"/>
    <polygon points="0,45 1200,15 1200,391 0,391" fill="var(--footer)"/>
  </svg>
  <div class="brand" style="left:110px;top:3715px;font-size:28px">
    <span class="brand-mark" style="width:30px;height:30px"></span>Étienne Roubaud Conseil
  </div>

  <p class="foot-head" style="left:598px;top:3633px">Quick Links</p>
  <ul class="foot-links">
    <li>Home</li><li>About us</li><li>Services</li><li>Blog</li><li>Contact</li>
  </ul>

  <p class="foot-head" style="left:780px;top:3633px">Contact Info</p>
  <svg class="abs" style="left:780px;top:3686px" width="10" height="14" viewBox="0 0 10 14"><path fill="var(--teal-soft)" d="M5 0a5 5 0 00-5 5c0 4 5 9 5 9s5-5 5-9a5 5 0 00-5-5zm0 7a2 2 0 110-4 2 2 0 010 4z"/></svg>
  <p class="foot-info" style="left:802px;top:3681px">2871 Lapierre Lane,<br>Montvale QC, Canada 4350</p>
  <svg class="abs" style="left:780px;top:3760px" width="12" height="12" viewBox="0 0 24 24"><path fill="var(--teal-soft)" d="M6.6 10.8a15 15 0 006.6 6.6l2.2-2.2c.3-.3.7-.4 1-.2 1.1.4 2.3.6 3.6.6.6 0 1 .4 1 1V20c0 .6-.4 1-1 1A17 17 0 013 4c0-.6.4-1 1-1h3.5c.6 0 1 .4 1 1 0 1.3.2 2.5.6 3.6.1.3 0 .7-.2 1z"/></svg>
  <p class="foot-info" style="left:804px;top:3754px">1 555 014 2090</p>
  <svg class="abs" style="left:780px;top:3810px" width="15" height="11" viewBox="0 0 24 18"><rect x="1" y="1" width="22" height="16" rx="2" fill="var(--teal-soft)"/><path d="M2 3l10 7 10-7" stroke="var(--footer)" stroke-width="2" fill="none"/></svg>
  <p class="foot-info" style="left:808px;top:3803px">info@etienneroubaud-conseil.com</p>

  <div class="foot-rule"></div>
  <p class="legal">© 2022, Étienne Roubaud Conseil. <strong>Privacy policy</strong> &nbsp;|&nbsp; <strong>Legal information</strong></p>
  <span class="social" style="left:939px" aria-label="Social network link"></span>
  <span class="social" style="left:992px" aria-label="Social network link"></span>
  <span class="social" style="left:1045px" aria-label="Social network link"></span>
</footer>

</body>
</html>
```